Flyer for an pediatric sleep consultancy - to distribute to play and childcare centers etc.

I need a flyer that will attract the attention of parents with children between the age of babies to toddlers, who may be experiencing sleep issues. The flyer will be placed at places such as community centers, doctors room, play centers, kindergardens, etc.

My company is called "The Quiet Meadow Nest" and provides a sleep consultancy service. My service essentially provides a customized plan for parents to follow and general advice and guidance. It is not medical advice.

I like to the flyer to have an overall tone that is soft and peaceful with a clean and beautiful design, however can catch the attention of parents who may be struggling with their child's sleep issues and are sleep deprived. I would like photos with minimal text. The colour I use is a brownish rose. I will attach some of my designs to give you an idea. You can have a look at my homepage as well to get an idea about my esthetic direction and the colour. Although the colour of my page is a bit too brownish....

I will provide the text to appear in the flyer once I have a better idea of the layout that I prefer for the flyer. The text however wont be extensive, just some catchy points.

I want to direct people to my website which is www.thequietmeadownest.example
I offer a first FREE evaluation call, to the parents, to get to know each other better, learn about their child's particular sleep problems and see if we are a good fit and can work together. I would like to have this information somehow on the flyer, so that the parents will contact me.
I also have a facebook page, which is: The Quiet Meadow Nest

I have a logo that I would like to appear on the flyer. I will attach the file once the uploader on pixel fair is fixed.

When I print the flyer - I like to print A5 SIZE ... please make sure the formatting is OK for this size.

Here are some text ideas. of course all of it would be too much, I guess. On the front of the flyer I would like to have some catchy phrase or something similar to get people interested and to want to know more. On the back there could be a bit more text and information. But I'm open too suggestions....
I'm not too sure about the wording yet. But here are some text that I might be use:

Is sleep an issue in your home?

Is your baby having trouble sleeping? ... are you?!
I can help!

Sleep, baby, sleep….

Teaching children how to sleep

The Quiet Meadow Nest is a pediatric sleep consultancy that specializes in helping parents with children who struggle to develop good and healthy sleep habits.
Disruptive sleep patterns or not enough sleep can affect the physical, mental and emotional development of your child.

Of course nobody plans to have a sleep problem, but habits can become easily ingrained and spiral quickly out of control and you can find yourself sleep deprived, desperate and not too sure what to do. You see all the other sleeping babies and wish there was someone who understood what you were going through?! Well, there is!

Contact me for a free 15 minute consultation.

This 15 minute „mini“ consultation is a chance to discuss your unique sleep challenges and sleep goals with me. I will provide you with an overview of how I will work with your family to achieve your wildest sleep dreams (goals).
Furthermore do I understand and believe that every child and their family is unique and there is no one size fits all!
I would love to have a chat with you and talk about how I can help make things easier for you and your family!

Do I need a sleep consultant for my child?
The answer is yes if:
- if your child will only fall asleep when nursing or bottle feeding
- if your child needs a dummy or other external aid, like being rocked, patted or taken for a care ride to fall asleep
- if your good night routine is a challenging and exhausting procedure instead of a relaxed and enjoyable moment for the whole family
- if sleep is a constant battle in your home which leaves you feeling frustrated and exhausted
- if your own lack of sleep is taking a toll on you and the whole family

What can I do for you?

I will:

- Guide you to set an age appropriate foundation for good sleep
- Create an individual sleep plan tailored especially to your child’s sleep needs and circumstances
- Help you to teach your childto go to sleep and get back to sleep independently during the night
- show you how to teach your child to take healthful, restorative naps
-Learn

Contact:

Marta Lindqvist
info@thequietmeadownest.example
www.thequietmeadownest.example
+34 612 384 570

Consultations in English, German or Spanish via Phone/CallNest or home consultation

Reason: I have to go on a business trip and won't be able to choose a design until the deadline. During the trip I won't have time to give feedback and ask for changes. thank you

Target Market(s)

parents, sleep deprived mothers, young families, child care provider,

Industry/Entity Type

Baby Care

Contact Information for Business Card

Marta Lindqvist
pediatric sleep consultant
+34 612 384 570

```html
<!DOCTYPE html>
<html lang="en">
<head>
<meta charset="utf-8">
<title>The Quiet Meadow Nest – Flyer</title>
<link rel="stylesheet" href="https://fonts.googleapis.com/css2?family=Noto+Serif&family=PT+Sans:wght@400;700&display=swap">
<style>
  :root{
    --backdrop:#3f3f41;
    --paper:#ffffff;
    --paper-grey:#ececec;
    --rose:#c9968c;
    --rose-soft:#f3c1b6;
    --rose-deep:#a7786f;
    --rose-head:#b87c72;
    --ink:#2f2f2f;
    --ink-soft:#444;
    --grey-logo:#8d9799;
    --arc-grey:#9b9b9b;
    --night:#2b2628;
    --skin:#e9c7b5;
    --skin-deep:#d6a48f;
  }
  *{box-sizing:border-box;margin:0;padding:0}
  html,body{width:1200px;height:822px;overflow:hidden;background:var(--backdrop)}
  .canvas{position:relative;width:1200px;height:822px}
  .page{position:absolute;top:68px;width:483px;height:685px;overflow:hidden;font-family:"PT Sans",sans-serif;color:var(--ink)}

  /* front */
  .front{left:96px;background:linear-gradient(180deg,#fff 0%,#f7f7f7 45%,#eeeeee 100%)}
  .brand{position:absolute;top:60px;left:0;width:100%;display:flex;justify-content:center;align-items:center;gap:10px}
  .brand-dot{width:22px;height:22px;border-radius:50%;background:var(--rose-soft)}
  .brand-name{font-family:"PT Sans",sans-serif;font-size:27px;font-weight:400;color:var(--grey-logo);letter-spacing:-.3px}
  .headline{position:absolute;left:30px;top:160px;font-family:"Noto Serif",serif;font-weight:400;font-size:28px;color:var(--ink);white-space:nowrap}
  .subline{position:absolute;left:30px;top:208px;font-family:"Noto Serif",serif;font-weight:400;font-size:24px;line-height:29px;color:var(--ink)}
  .front-art{position:absolute;left:0;top:0;width:483px;height:685px}
  .tagline{position:absolute;left:300px;top:583px;width:182px;text-align:center;color:#fff;font-size:17.5px;line-height:22px}
  .front-footer{position:absolute;left:0;bottom:0;width:100%;height:39px;background:var(--rose-deep);color:#fff;font-size:16px;display:flex;align-items:center;justify-content:center}

  /* back */
  .back{left:599px;background:linear-gradient(180deg,#fafafa 0%,#f0f0f0 60%,#e9e9e9 100%)}
  .intro{position:absolute;left:0;top:0;width:100%;height:224px;padding:20px 21px 0 21px;background:linear-gradient(120deg,#f2a99c 0%,#f6c3b8 45%,#fbe4de 75%,#fff 100%);font-size:9.9px;line-height:13.2px;color:var(--ink)}
  .intro p{margin-bottom:7px}
  .intro .cta{font-weight:700}
  .portrait{position:absolute;right:0;top:286px;width:200px;height:370px}
  .qa{position:absolute;left:21px;top:232px;width:340px}
  .qa h2{font-size:13px;font-weight:700;color:var(--rose-head);margin-bottom:5px}
  .qa h3{font-size:10.4px;font-weight:700;color:var(--ink)}
  .qa ul{list-style:none;font-size:10.4px;line-height:13.8px;color:var(--ink);margin-bottom:12px}
  .qa li{position:relative;padding-left:12px}
  .qa li::before{content:"";position:absolute;left:1px;top:5px;width:5px;height:5px;border-radius:50%;background:var(--rose)}
  .qa .needs{width:340px}
  .qa .needs li:nth-child(n+3){width:240px}
  .qa .offers{width:290px}
  .contact-band{position:absolute;left:0;top:600px;width:300px;height:56px;background:linear-gradient(90deg,#fff 70%,rgba(255,255,255,0))}
  .mini-brand{position:absolute;left:168px;top:580px;font-size:9px;color:var(--grey-logo)}
  .contact{position:absolute;left:34px;top:592px;font-size:10.4px;line-height:13.8px;color:var(--ink)}
  .contact .name{font-weight:700}
  .back-footer{position:absolute;left:0;bottom:0;width:100%;height:29px;background:var(--night);color:var(--rose-soft);font-size:10.8px;display:flex;align-items:center;justify-content:center}
</style>
</head>
<body>
<div class="canvas">

  <section class="page front">
    <svg class="front-art" viewBox="0 0 483 685" aria-hidden="false">
      <defs>
        <clipPath id="front-photo-area"><rect x="0" y="0" width="483" height="646"/></clipPath>
        <radialGradient id="child-tone" cx="55%" cy="45%" r="60%">
          <stop offset="0" stop-color="#f1d6c7"/>
          <stop offset=".6" stop-color="#dcb3a0"/>
          <stop offset="1" stop-color="#b58a72"/>
        </radialGradient>
        <linearGradient id="sleep-tone" x1="0" y1="0" x2="1" y2="1">
          <stop offset="0" stop-color="#d9ab97"/>
          <stop offset=".5" stop-color="#efd2c4"/>
          <stop offset="1" stop-color="#f7ece6"/>
        </linearGradient>
        <path id="lullaby-arc" d="M 24 410 A 250 250 0 0 1 325 470"/>
      </defs>
      <g clip-path="url(#front-photo-area)">
        <g role="img" aria-label="Photo of a smiling curly-haired toddler">
          <circle cx="430" cy="470" r="215" fill="url(#child-tone)"/>
        </g>
        <circle cx="120" cy="690" r="262" fill="#fff"/>
        <g role="img" aria-label="Photo of a mother resting her head beside her sleeping baby">
          <circle cx="120" cy="690" r="242" fill="url(#sleep-tone)"/>
        </g>
        <path d="M 262 646 C 292 566 372 540 483 540 L 483 646 Z" fill="var(--rose)"/>
      </g>
      <text font-family="PT Sans, sans-serif" font-size="27" font-weight="700" fill="var(--arc-grey)">
        <textPath href="#lullaby-arc">Sleep, baby, sleep....</textPath>
      </text>
    </svg>

    <div class="brand">
      <span class="brand-dot"></span>
      <span class="brand-name">The Quiet Meadow Nest</span>
    </div>
    <h1 class="headline">Is sleep an issue in your home?</h1>
    <p class="subline">Is your baby having<br>trouble sleeping? ... are you?!<br>I can help!</p>
    <p class="tagline">Teaching children<br>how to sleep</p>
    <footer class="front-footer">www.thequietmeadownest.example</footer>
  </section>

  <section class="page back">
    <div class="intro">
      <p>The Quiet Meadow Nest is a pediatric sleep consultancy that specializes in helping parents with children who struggle to develop good and healthy sleep habits. Disruptive sleep patterns or not enough sleep can affect the physical, mental and emotional development of your child.</p>
      <p>Of course nobody plans to have a sleep problem, but habits can become easily ingrained and spiral quickly out of control and you can find yourself sleep deprived, desperate and not too sure what to do. You see all the other sleeping babies and wish there was someone who understood what you were going through?! Well, there is!</p>
      <p class="cta">Contact me for a free 15 minute consultation.</p>
      <p>This 15 minute „mini“ consultation is a chance to discuss your unique sleep challenges and sleep goals with me. I will provide you with an overview of how I will work with your family to achieve your wildest sleep dreams (goals). Furthermore do I understand and believe that every child and their family is unique and there is no one size fits all! I would love to have a chat with you and talk about how I can help make things easier for you and your family!</p>
    </div>

    <svg class="portrait" viewBox="0 0 200 370" role="img" aria-label="Photo of the consultant holding a toddler">
      <defs>
        <linearGradient id="portrait-tone" x1="0" y1="0" x2="0" y2="1">
          <stop offset="0" stop-color="#e7cdb0"/>
          <stop offset=".35" stop-color="#eccbbb"/>
          <stop offset=".6" stop-color="#c9d3df"/>
          <stop offset="1" stop-color="#2e2c30"/>
        </linearGradient>
      </defs>
      <path d="M 40 70 C 60 10 150 -10 200 20 L 200 370 L 10 370 C 0 300 20 200 40 70 Z" fill="url(#portrait-tone)"/>
    </svg>

    <div class="qa">
      <h2>Do I need a sleep consultant for my child?</h2>
      <h3>The answer is yes if:</h3>
      <ul class="needs">
        <li>if your child will only fall asleep when nursing or bottle feeding</li>
        <li>if your child needs a dummy or other external aid, like being rocked, patted or taken for a care ride to fall asleep</li>
        <li>if your good night routine is a challenging and exhausting procedure instead of a relaxed and enjoyable moment for the whole family</li>
        <li>if sleep is a constant battle in your home which leaves you feeling frustrated and exhausted</li>
        <li>if your own lack of sleep is taking a toll on you and the whole family</li>
      </ul>
      <h2>What can I do for you?</h2>
      <h3>I will:</h3>
      <ul class="offers">
        <li>Guide you to set an age appropriate foundation for good sleep</li>
        <li>Create an individual sleep plan tailored especially to your child’s sleep needs and circumstances</li>
        <li>Help you to teach your childto go to sleep and get back to sleep independently during the night</li>
        <li>show you how to teach your child to take healthful, restorative naps</li>
        <li>Learn</li>
      </ul>
    </div>

    <div class="contact-band"></div>
    <p class="mini-brand">The Quiet Meadow Nest</p>
    <address class="contact" style="font-style:normal">
      <span class="name">Marta Lindqvist</span><br>
      info@thequietmeadownest.example<br>
      www.thequietmeadownest.example<br>
      +34 612 384 570
    </address>
    <footer class="back-footer">Consultations in English, German or Spanish via Phone/CallNest or home consultation</footer>
  </section>

</div>
</body>
</html>
```